Holiday Rental Company Flyer Design (DL not A5)

Note from PixelFolk Administration: The category sizing selected is A5, however the project requires DL sized artwork. Please refer to the DL template link below while the 'Special Requirements' are updated accordingly.

Project Brief:
We need a double sided DL flyer designed for an up market Holiday Rental Company that portrays a personalised approach to property management. These are to be used for letter box drops to homes we're specifically targeting so the design should be modern, complimentary colour palette, uncluttered & visually appealing.

Please Download the DL Template from Quillmark here: http://www.quillmark.com.au/qm/ns/propath/UploadResources.aspx?selectedTab=0?pfid=BFB&pf_id=BFB&xnav=easypath-upload-image#Templates

Target Market(s)

Wealthy Home Owners

Industry/Entity Type

It Company

Font styles to use
Other font styles liked:
• Avant Garde Extra Light & Demi

Colors
33b8a4

Requirements
Must have
• DL Flyer sizes (210mm width x 99mm width, plus 3mm bleed)
• Front: Logo, Main Image & Grab
• Back: Contact Details & Brief Description of our business
• Images: Ideally the main image should be the house with the pool but alternatively a lifestyle images could also be used.
Nice to have
• A creative designer!
Should not have
• Clutter & busy designs

```html
<!DOCTYPE html>
<html lang="en">
<head>
<meta charset="utf-8">
<title>Coastal Haven – Holiday Rental Management DL Flyer</title>
<link rel="stylesheet" href="https://fonts.googleapis.com/css2?family=Raleway:wght@200;300;700&family=Roboto+Condensed:wght@300;400&display=swap">
<style>
  :root {
    --teal: #22b08f;
    --teal-dark: #1a9c7e;
    --ink: #4a4a4a;
    --white: #ffffff;
    --stage: #e4e4e4;
    --strip: #6b6b6b;
    --sky-top: #1c1850;
    --sky-mid: #5a4aa8;
    --pool-top: #3f7fd6;
    --pool-bottom: #2a5fbf;
  }
  * { margin: 0; padding: 0; box-sizing: border-box; }
  html, body { width: 1200px; height: 1169px; overflow: hidden; }
  body { background: var(--stage); position: relative; font-family: 'Roboto Condensed', sans-serif; }

  .flyer { position: absolute; top: 57px; width: 500px; height: 1044px; overflow: hidden; }
  .flyer--front { left: 53px; }
  .flyer--back { left: 620px; background: var(--white); }

  /* Front */
  .front-band { position: absolute; left: 0; width: 100%; height: 17px; background: var(--teal); z-index: 2; }
  .front-band--top { top: 0; }
  .front-band--bottom { bottom: 0; }
  .hero-photo {
    position: absolute; inset: 0;
    background: linear-gradient(180deg, var(--sky-top) 0%, #3a2f86 22%, var(--sky-mid) 38%, #8a7cc4 46%, var(--pool-top) 52%, #4a8de0 65%, var(--pool-bottom) 100%);
  }
  .front-brand {
    position: absolute; left: 0; width: 100%; top: 626px; text-align: center;
    font-family: 'Raleway', sans-serif; font-weight: 200; color: var(--white);
    font-size: 54px; line-height: 54px; letter-spacing: 6px;
  }
  .front-tagline { position: absolute; left: 88px; top: 842px; color: var(--white); font-family: 'Raleway', sans-serif; font-weight: 700; }
  .front-tagline__line1 { font-size: 34px; line-height: 36px; letter-spacing: 1.5px; }
  .front-tagline__line2 { font-size: 41px; line-height: 40px; letter-spacing: 1px; }
  .front-tagline__line3 { font-size: 18px; line-height: 28px; letter-spacing: 8.6px; }

  /* Back */
  .intro-heading {
    position: absolute; left: 44px; top: 58px; width: 440px;
    font-family: 'Raleway', sans-serif; font-weight: 700; color: var(--teal);
    font-size: 21.5px; line-height: 26px; text-transform: uppercase;
  }
  .intro-copy {
    position: absolute; left: 44px; top: 163px; width: 412px;
    font-size: 14.6px; line-height: 20.6px; font-weight: 300; color: var(--ink);
  }
  .diff-heading {
    position: absolute; left: 43px; top: 291px;
    font-family: 'Raleway', sans-serif; font-weight: 200; color: var(--teal);
    font-size: 31px; line-height: 36px;
  }
  .diff-copy {
    position: absolute; left: 44px; top: 330px; width: 400px;
    font-size: 12.6px; line-height: 17.6px; font-weight: 300; color: var(--ink);
  }
  .diff-list { position: absolute; left: 44px; top: 399px; list-style: none; font-size: 12.6px; line-height: 17.6px; font-weight: 300; color: var(--ink); }
  .diff-list li { padding-left: 14px; position: relative; }
  .diff-list li::before { content: ""; position: absolute; left: 1px; top: 7px; width: 5px; height: 5px; border-radius: 50%; background: var(--teal); }

  .gallery { position: absolute; left: 0; top: 494px; width: 500px; height: 396px; display: grid; grid-template-columns: 251px 249px; grid-template-rows: 212px 184px; }
  .gallery__photo--exterior { background: linear-gradient(180deg, #2b2f66 0%, #4a4d86 45%, #6b5a44 75%, #2a2622 100%); }
  .gallery__photo--lounge { background: linear-gradient(160deg, #9a9490 0%, #d8d3cc 45%, #bfb7ae 75%, #6f6862 100%); }
  .gallery__photo--bedroom { background: linear-gradient(180deg, #c7ccd0 0%, #eef0f0 50%, #9aa6a8 78%, #5c5750 100%); }
  .gallery__photo--dining { background: linear-gradient(170deg, #cfcfcc 0%, #e6e4e0 45%, #a69886 75%, #4d4640 100%); }

  .contact-strip {
    position: absolute; left: 0; top: 890px; width: 500px; height: 30px; background: var(--strip);
    color: #ececec; font-size: 10.5px; line-height: 30px; text-align: center; font-weight: 300;
  }
  .footer { position: absolute; left: 0; top: 920px; width: 500px; height: 124px; background: var(--teal); color: var(--white); }
  .footer-brand { position: absolute; left: 42px; top: 30px; width: 190px; text-align: center; }
  .footer-brand__name { font-family: 'Raleway', sans-serif; font-weight: 200; font-size: 21px; line-height: 22px; letter-spacing: 2.5px; }
  .footer-brand__address { font-size: 11px; line-height: 14px; margin-top: 10px; font-weight: 300; }
  .footer-contact { position: absolute; right: 30px; top: 42px; text-align: right; }
  .footer-contact__phone { font-size: 17px; line-height: 20px; font-weight: 400; }
  .footer-contact__line { font-family: 'Raleway', sans-serif; font-weight: 700; font-size: 13.2px; line-height: 17px; }
</style>
</head>
<body>
  <section class="flyer flyer--front">
    <div class="hero-photo" role="img" aria-label="Night view of a modern luxury home with lit interiors beside a long blue pool and wall water feature"></div>
    <div class="front-band front-band--top"></div>
    <h1 class="front-brand">COASTAL<br>HAVEN</h1>
    <div class="front-tagline">
      <div class="front-tagline__line1">HOLIDAY RENTAL</div>
      <div class="front-tagline__line2">MANAGEMENT</div>
      <div class="front-tagline__line3">WITH A DIFFERENCE</div>
    </div>
    <div class="front-band front-band--bottom"></div>
  </section>

  <section class="flyer flyer--back">
    <h2 class="intro-heading">At Coastal Haven, we endeavour to make the process of holiday letting your property as enjoyable and rewarding as possible.</h2>
    <p class="intro-copy">For owners who are time poor, we have experienced people on hand to relieve some of this pressure. Our dedicated team can give styling tips, co-ordinate photo shoots, organise your linen set up and much more. If you’re thinking of utilising your property for the holiday rental market, don’t hesitate to contact us.</p>

    <h2 class="diff-heading">WHAT WE DO DIFFERENTLY!</h2>
    <p class="diff-copy">Rather than relying upon a key safe or a central pick-up destination, a ‘Coastal Haven’ staff member will greet guests upon arrival. Our ‘Meet &amp; Greet’ service provides home owners with an increased level of Security and also allows us to:</p>
    <ul class="diff-list">
      <li>Prepare the home for their arrival (lights, heaters, music etc.)</li>
      <li>Establish a rapport &amp; help facilitate future bookings.</li>
      <li>Reiterate their responsibilities to ensure the return of their bond</li>
    </ul>

    <div class="gallery">
      <div class="gallery__photo--exterior" role="img" aria-label="Modern two-storey home lit at dusk with landscaped garden"></div>
      <div class="gallery__photo--lounge" role="img" aria-label="Living room with white sectional sofa and colourful artwork"></div>
      <div class="gallery__photo--bedroom" role="img" aria-label="Bright bedroom with white bed, teal accents and water views"></div>
      <div class="gallery__photo--dining" role="img" aria-label="Open plan dining area with timber table and white chairs"></div>
    </div>

    <p class="contact-strip">If you’d like to know what your property could achieve or require additional information, please contact us at:</p>

    <footer class="footer">
      <div class="footer-brand">
        <div class="footer-brand__name">COASTAL<br>HAVEN</div>
        <div class="footer-brand__address">PO Box 18, Tidewater Victoria 3950</div>
      </div>
      <div class="footer-contact">
        <div class="footer-contact__phone">Phone: (03)5900 4172</div>
        <div class="footer-contact__line">stay@coastalhaven.com.au</div>
        <div class="footer-contact__line">www.coastalhaven.com.au</div>
      </div>
    </footer>
  </section>
</body>
</html>
```